MS word document templates for consultancy

I need the following templates for my business using my logo as branding.

- General report template
- Letter head template
- Tender proposal template

The templates should be sleek and with minimal colors, but with a small amount of green and grey where appropriate (as per attached logo and email signature). Font should be consistent with the text in the email signature.

```html
<!DOCTYPE html>
<html lang="en">
<head>
<meta charset="utf-8">
<title>Northlane Advisory – Document Templates</title>
<link href="https://fonts.googleapis.com/css2?family=Montserrat:wght@400;500;600;700&family=Arimo:wght@400&display=swap" rel="stylesheet">
<style>
  :root{
    --stage-dark:#4b4b4b;
    --stage-mid:#858585;
    --paper:#f1f1f1;
    --ink:#1d1d1d;
    --text-grey:#707070;
    --body-grey:#666666;
    --rule-grey:#8a8a8a;
    --signature-tone:#dedede;
    --brand-green:#1f9a3c;
  }
  *{box-sizing:border-box;margin:0;padding:0}
  html,body{width:1200px;height:2668px;overflow:hidden}
  body{font-family:"Montserrat",sans-serif;color:var(--ink)}
  .stage{position:relative;width:1200px;overflow:hidden}
  .stage--letter{height:890px;background:var(--stage-dark)}
  .stage--report,.stage--tender{height:889px;background:var(--stage-mid)}

  .page{position:absolute;background:var(--paper);box-shadow:0 10px 24px rgba(0,0,0,.28)}
  .brand-name{font-family:"Montserrat",sans-serif;font-weight:500;color:var(--ink);letter-spacing:-.2px;white-space:nowrap}

  /* letterhead */
  .letterhead{left:396px;top:165px;width:408px;height:575px;padding:20px 42px 0 40px}
  .letterhead .brand-name{font-size:19px}
  .letter-subject{margin-top:86px;font-size:10.5px;font-weight:600;color:var(--text-grey);letter-spacing:.6px}
  .letter-sender{margin-top:19px;font-size:10.5px;font-weight:700;color:#555}
  .letter-role{font-size:8px;color:var(--text-grey);margin-top:2px}
  .letter-body{margin-top:12px;font-size:6.4px;line-height:8.6px;color:var(--body-grey);text-align:justify}
  .letter-body p{margin-bottom:17px}
  .letter-body p:last-child{margin-bottom:0}
  .signature{margin-top:30px;width:86px;height:22px;background:linear-gradient(90deg,var(--signature-tone),#eaeaea)}
  .letter-date{margin-top:4px;font-size:9px;color:#444}

  .page-footer{position:absolute;left:0;right:0;bottom:0}
  .contact-row{display:flex;justify-content:space-between;padding:0 42px 8px 40px;font-size:7px;color:var(--text-grey);line-height:1.6}
  .contact-row .right{text-align:right}
  .contact-row svg{vertical-align:middle}
  .footer-band{display:block;width:100%}

  /* covers */
  .cover{width:300px;height:420px;padding:36px 30px 0}
  .cover .brand-name{font-size:17px}
  .cover--back{left:380px;top:190px}
  .cover--front{left:500px;top:250px;box-shadow:0 12px 28px rgba(0,0,0,.32)}
  .cover-title{font-family:"Arimo",sans-serif;text-align:center;margin-top:96px;line-height:1.05}
  .cover-year{font-size:20px;color:var(--ink)}
  .cover-main{font-size:28px;color:var(--brand-green);margin-top:6px}
  .cover-sub{font-size:17px;color:var(--brand-green)}
  .cover .contact-row{padding:0 30px 6px;font-size:5.5px}
</style>
</head>
<body>

<section class="stage stage--letter">
  <article class="page letterhead">
    <div class="brand-name">Northlane Advisory</div>
    <div class="letter-subject">SUBJECT</div>
    <div class="letter-sender">Dana Reyes</div>
    <div class="letter-role">Managing Director</div>
    <div class="letter-body">
      <p>Lorem ipsum is simply placeholder text used across the printing and typesetting trade. It has served as the standard filler text for many years, ever since an early printer took a tray of type and scrambled it to make a sample sheet. It has survived many decades and also the leap into digital typesetting, remaining essentially unchanged. It became widely known through printed transfer sheets carrying lorem ipsum passages, and more recently through desktop layout software that ships with versions of lorem ipsum.</p>
      <p>Contrary to popular belief, lorem ipsum is not simply random text. It has roots in a piece of classical Latin writing from long ago, making it well over a thousand years old.</p>
      <p>A visiting scholar at a small regional college looked up one of the more obscure Latin words, consectetur, from a lorem ipsum passage, and going through the uses of the word in classical writing, traced the undoubted source. Lorem ipsum comes from sections</p>
      <p>Contrary to popular belief, lorem ipsum is not simply random text. It has roots in a piece of classical Latin writing from long ago, making it well over a thousand years old.</p>
    </div>
    <div class="signature" role="img" aria-label="Handwritten signature of Dana Reyes"></div>
    <div class="letter-date">23/01/2025</div>

    <footer class="page-footer">
      <div class="contact-row">
        <div>
          <div><svg width="6" height="6" viewBox="0 0 10 10"><path d="M2 1l2 2-1 1.5c.8 1.5 1.7 2.4 3 3L7.5 6l2 2-1.5 1.5C4 9 1 6 .5 2.5z" fill="#8a8a8a"/></svg> 0400 555 019</div>
          <div><svg width="6" height="6" viewBox="0 0 10 10"><path d="M5 0a3.5 3.5 0 0 0-3.5 3.5C1.5 6 5 10 5 10s3.5-4 3.5-6.5A3.5 3.5 0 0 0 5 0z" fill="#8a8a8a"/></svg> Dummy City, Dummy Country</div>
        </div>
        <div class="right">
          <div>info@northlaneadvisory.com <svg width="6" height="6" viewBox="0 0 10 10"><rect x="1" y="2" width="8" height="6" fill="#8a8a8a"/></svg></div>
          <div>www.northlaneadvisory.com <svg width="6" height="6" viewBox="0 0 10 10"><circle cx="5" cy="5" r="4" fill="#8a8a8a"/></svg></div>
        </div>
      </div>
      <svg class="footer-band" viewBox="0 0 408 14" preserveAspectRatio="none" height="14">
        <rect x="0" y="2" width="408" height="3" fill="var(--rule-grey)"/>
        <polygon points="165,0 235,0 245,6 408,6 408,14 0,14 0,6 155,6" fill="var(--brand-green)"/>
      </svg>
    </footer>
  </article>
</section>

<section class="stage stage--report">
  <article class="page cover cover--back">
    <div class="brand-name">Northlane Advisory</div>
    <footer class="page-footer">
      <svg class="footer-band" viewBox="0 0 300 10" preserveAspectRatio="none" height="10">
        <rect x="0" y="1" width="300" height="2" fill="var(--rule-grey)"/>
        <polygon points="120,0 180,0 188,4 300,4 300,10 0,10 0,4 112,4" fill="var(--brand-green)"/>
      </svg>
    </footer>
  </article>
  <article class="page cover cover--front">
    <div class="brand-name">Northlane Advisory</div>
    <div class="cover-title">
      <div class="cover-year">2025</div>
      <div class="cover-main">General</div>
      <div class="cover-sub">Report</div>
    </div>
    <footer class="page-footer">
      <div class="contact-row">
        <div><div>0400 555 019</div><div>Dummy City, Dummy Country</div></div>
        <div class="right"><div>info@northlaneadvisory.com</div><div>www.northlaneadvisory.com</div></div>
      </div>
      <svg class="footer-band" viewBox="0 0 300 10" preserveAspectRatio="none" height="10">
        <rect x="0" y="1" width="300" height="2" fill="var(--rule-grey)"/>
        <polygon points="120,0 180,0 188,4 300,4 300,10 0,10 0,4 112,4" fill="var(--brand-green)"/>
      </svg>
    </footer>
  </article>
</section>

<section class="stage stage--tender">
  <article class="page cover cover--back">
    <div class="brand-name">Northlane Advisory</div>
    <footer class="page-footer">
      <svg class="footer-band" viewBox="0 0 300 10" preserveAspectRatio="none" height="10">
        <rect x="0" y="1" width="300" height="2" fill="var(--rule-grey)"/>
        <polygon points="120,0 180,0 188,4 300,4 300,10 0,10 0,4 112,4" fill="var(--brand-green)"/>
      </svg>
    </footer>
  </article>
  <article class="page cover cover--front">
    <div class="brand-name">Northlane Advisory</div>
    <div class="cover-title">
      <div class="cover-year">2025</div>
      <div class="cover-main">Tender</div>
      <div class="cover-sub">proposal</div>
    </div>
    <footer class="page-footer">
      <div class="contact-row">
        <div><div>0400 555 019</div><div>Dummy City, Dummy Country</div></div>
        <div class="right"><div>info@northlaneadvisory.com</div><div>www.northlaneadvisory.com</div></div>
      </div>
      <svg class="footer-band" viewBox="0 0 300 10" preserveAspectRatio="none" height="10">
        <rect x="0" y="1" width="300" height="2" fill="var(--rule-grey)"/>
        <polygon points="120,0 180,0 188,4 300,4 300,10 0,10 0,4 112,4" fill="var(--brand-green)"/>
      </svg>
    </footer>
  </article>
</section>

</body>
</html>
```